Etiketten-Design für Wein
Zielgruppe
Wir produzieren Wein und sind auf der Suche nach einer innovativen Weinetikette, welche sich durch unsere Weinvariationen durchziehen lässt.
Für das stehen wir ein: Nachhaltigkeit, moderne Landwirtschaft, Familienbetrieb, zukunftsorientiert, im Einklang mi der Natur, Freude an Pflanzen und Tieren.
Was uns gefällt: Relief / Prägung, eher schlichte, moderne und edle Etiketten, allenfalls Elemente aus der Natur, die auf Nachhaltigkeit hinweisen
Das möchten wir nicht auf der Etikette: zu knallige Farben, Comicfiguren oder ähnliches.
Unsere Weine werden direkt vermarktet und sollen aufgrund ihrer Etikette aus dem Weinregal herausstechen und ein Eyecatcher für die Kund:innen sein. Auch in einem Restaurant sollen sie als edlen Wein präsentiert werden können. Wir möchten, dass die Weinetiketten ein Storytelling mit sich bringen in Bezug auf die obenstehenden Punkte, für die wir einstehen.
Unsere Zielgruppe: Qualitätsbewusste Weingeniesser, mittleren und jüngeren Alters
Aufgabenstellung
Folgende Angaben sind auf der Etikette erforderlich:
- Weinsorte: Reserva / Riesling / Blauburgunder / Federweisser
- Name: Brunnegut (kann klein und schlicht, unauffällig sein)
Unser Logo kann in Etikette aufgegriffen werden (auch in angepasster Form), ist aber nicht zwingend nötig. Das Logo ist auch eher revisionsbedürftig. ????
Folgende Masse sollte die Etikette ca. haben:
- Breite 95 mm
- Höhe 80 mm

```html
<!DOCTYPE html>
<html lang="de">
<head>
<meta charset="utf-8">
<title>Brunnegut – Etiketten 2023</title>
<link rel="stylesheet" href="https://fonts.googleapis.com/css2?family=Jost:wght@300;400&family=Libre+Baskerville:wght@700&family=Roboto+Slab:wght@400&display=swap">
<style>
  :root {
    --page: #ffffff;
    --label: #f1f1f1;
    --ink: #1c1c1c;
    --feder: #b3b51c;
    --feder-art: #d8dbae;
    --riesling: #b09a1e;
    --riesling-art: #ddd3a6;
    --blau: #2a1a25;
    --blau-art: #aba1ab;
    --riserva: #4b1014;
    --riserva-art: #c2b3b8;
  }
  * { margin: 0; padding: 0; box-sizing: border-box; }
  html, body {
    width: 1200px;
    height: 1200px;
    overflow: hidden;
    background: var(--page);
  }
  .label-set {
    width: 1200px;
    height: 1200px;
    display: grid;
    grid-template-columns: repeat(2, 480px);
    grid-template-rows: repeat(2, 404px);
    gap: 60px;
    justify-content: center;
    align-content: center;
  }
  .label {
    position: relative;
    background: var(--label);
    overflow: hidden;
    box-shadow: 0 1px 3px rgba(0,0,0,0.08);
    text-align: center;
  }
  .label__art {
    position: absolute;
    left: 50%;
    top: 18px;
    width: 230px;
    height: 386px;
    transform: translateX(-50%);
    border-radius: 48% 52% 40% 44%;
  }
  .label--feder .label__art { background: radial-gradient(ellipse at 50% 55%, var(--feder-art) 0%, rgba(216,219,174,0.35) 55%, rgba(216,219,174,0) 75%); }
  .label--riesling .label__art { background: radial-gradient(ellipse at 50% 60%, var(--riesling-art) 0%, rgba(221,211,166,0.35) 55%, rgba(221,211,166,0) 75%); }
  .label--blau .label__art { background: radial-gradient(ellipse at 50% 70%, var(--blau-art) 0%, rgba(171,161,171,0.35) 55%, rgba(171,161,171,0) 75%); width: 300px; }
  .label--riserva .label__art { background: radial-gradient(ellipse at 50% 55%, var(--riserva-art) 0%, rgba(194,179,184,0.35) 55%, rgba(194,179,184,0) 75%); }
  .label__place {
    position: absolute;
    top: 44px;
    left: 0; right: 0;
    font-family: "Jost", sans-serif;
    font-weight: 300;
    font-size: 16px;
    letter-spacing: 0.28em;
    color: var(--ink);
  }
  .label__brand {
    position: absolute;
    top: 72px;
    left: 0; right: 0;
    font-family: "Libre Baskerville", serif;
    font-weight: 700;
    font-size: 21px;
    letter-spacing: 0.2em;
    color: var(--ink);
  }
  .label__wine {
    position: absolute;
    left: 0; right: 0;
    top: 50%;
    transform: translateY(-46%);
    font-family: "Roboto Slab", serif;
    font-weight: 400;
    font-size: 60px;
    line-height: 1.1;
    letter-spacing: 0.05em;
  }
  .label--riesling .label__wine,
  .label--riserva .label__wine { letter-spacing: 0.13em; }
  .label--feder .label__wine { color: var(--feder); }
  .label--riesling .label__wine { color: var(--riesling); }
  .label--blau .label__wine { color: var(--blau); }
  .label--riserva .label__wine { color: var(--riserva); }
  .label__year {
    position: absolute;
    bottom: 44px;
    left: 0; right: 0;
    font-family: "Jost", sans-serif;
    font-weight: 400;
    font-size: 18px;
    letter-spacing: 0.3em;
    color: var(--ink);
  }
</style>
</head>
<body>
  <main class="label-set">
    <section class="label label--feder">
      <div class="label__art" role="img" aria-label="Pinselzeichnung einer Weinrebe in zartem Grün"></div>
      <p class="label__place">TALBACH</p>
      <p class="label__brand">BRUNNEGUT</p>
      <h2 class="label__wine">FEDER<br>WEISER</h2>
      <p class="label__year">2023</p>
    </section>
    <section class="label label--riesling">
      <div class="label__art" role="img" aria-label="Pinselzeichnung einer Weinrebe in hellem Gold"></div>
      <p class="label__place">TALBACH</p>
      <p class="label__brand">BRUNNEGUT</p>
      <h2 class="label__wine">RIESLING</h2>
      <p class="label__year">2023</p>
    </section>
    <section class="label label--blau">
      <div class="label__art" role="img" aria-label="Pinselzeichnung eines Rebstocks in Graumauve"></div>
      <p class="label__place">TALBACH</p>
      <p class="label__brand">BRUNNEGUT</p>
      <h2 class="label__wine">BLAU<br>BURGUNDER</h2>
      <p class="label__year">2023</p>
    </section>
    <section class="label label--riserva">
      <div class="label__art" role="img" aria-label="Pinselzeichnung einer Weinrebe in Altrosa"></div>
      <p class="label__place">TALBACH</p>
      <p class="label__brand">BRUNNEGUT</p>
      <h2 class="label__wine">RISERVA</h2>
      <p class="label__year">2023</p>
    </section>
  </main>
</body>
</html>
```